Business Card Design

I am a florist specialising in weddings. I would like a very modern however elegant and simple design. My arrangement designs can be quite rustic with a vintage feel, so if you are able to reflect this in the card that would be great.
Updates

Thank you everyone for your submissions. I have found some further words for inspiration. I am looking for something more earthy and artisan looking. If possible I would like to use 100% recycled paper - the type that even looks rustic and recycled. I may even opt to use a small logo to emphasis the fact that they are made from recycled paper. I know this is quite different to my original brief but I wasn't quite sure what to expect from your designs. Also, with the logo, I give permission for it to be cropped to remove the 'Floral Designer' text. Please contact me if you need any further assistance. Many thanks Lorna-Jayne Petal & Thread

I would prefer not to have any photgraphs & not too much pink. Thank you!

Industry/Entity Type

Florist

Contact Information for Business Card

Lorna-Jayne Tulk
Floral Designer
0417 635 208
lornajayne@petalandthread.com.au
petalandthread.com.au

Requirements
Must have
• My logo

```html
<!DOCTYPE html>
<html lang="en">
<head>
<meta charset="utf-8">
<title>Petal &amp; Thread — Business Card</title>
<link rel="stylesheet" href="https://fonts.googleapis.com/css2?family=Lato:wght@400;700;900&display=swap">
<style>
  :root {
    --page-bg: #2a2a2a;
    --card-bg: #f7f7f7;
    --card-stripe: rgba(0, 0, 0, 0.025);
    --ink: #1a1a1a;
    --ink-soft: #6e6e6e;
    --ink-muted: #8a8a8a;
    --service-ink: #4a4a4a;
    --divider-top: #d8d8d8;
    --divider-bottom: #7a7a7a;
    --photo-lilac: #9c8fb8;
    --photo-wood: #a8643a;
    --photo-peach: #e4a57f;
    --photo-green: #4c6b3a;
    --photo-blue: #6f8fb4;
  }

  * { box-sizing: border-box; margin: 0; padding: 0; }

  html, body {
    width: 1200px;
    height: 900px;
    overflow: hidden;
    background: var(--page-bg);
    font-family: "Lato", Arial, sans-serif;
  }

  .sheet {
    width: 1200px;
    height: 900px;
    display: flex;
    flex-direction: column;
    align-items: center;
    justify-content: center;
    gap: 36px;
  }

  .card {
    position: relative;
    width: 660px;
    height: 377px;
    background:
      repeating-linear-gradient(135deg, var(--card-stripe) 0 1px, transparent 1px 4px),
      var(--card-bg);
    overflow: hidden;
  }

  /* ---------- Back: services ---------- */
  .services-photos {
    position: absolute;
    top: 22px;
    left: 22px;
    right: 22px;
    height: 200px;
    display: flex;
    gap: 14px;
  }

  .services-photo { flex: 1; border-radius: 16px; }

  .services-photo--posy {
    background: linear-gradient(160deg, var(--photo-lilac) 0%, #c9c3d6 45%, var(--photo-wood) 100%);
  }
  .services-photo--roses {
    background: linear-gradient(170deg, var(--photo-peach) 0%, #f2e6dc 50%, var(--photo-green) 100%);
  }
  .services-photo--table {
    background: linear-gradient(150deg, var(--photo-blue) 0%, #c7d3e2 60%, #e9ecef 100%);
  }

  .services-list {
    position: absolute;
    left: 0;
    right: 0;
    top: 248px;
    text-align: center;
    color: var(--service-ink);
    font-weight: 900;
    font-size: 21px;
    line-height: 1.4;
  }

  /* ---------- Front: contact ---------- */
  .brand {
    position: absolute;
    left: 18px;
    top: 176px;
    width: 264px;
    text-align: center;
    color: var(--ink);
  }

  .brand-name {
    display: flex;
    align-items: center;
    justify-content: center;
    gap: 8px;
    white-space: nowrap;
    font-weight: 400;
    font-size: 31px;
    line-height: 1;
  }

  .brand-dot {
    width: 10px;
    height: 10px;
    border-radius: 50%;
    background: var(--ink);
    flex: none;
  }

  .brand-tagline {
    margin-top: 14px;
    font-size: 18px;
    font-weight: 400;
  }

  .holder {
    position: absolute;
    left: 300px;
    top: 56px;
  }

  .holder-name {
    font-weight: 900;
    font-size: 22px;
    color: var(--ink);
    letter-spacing: 0.3px;
  }

  .holder-role {
    font-size: 14px;
    color: var(--ink-muted);
    letter-spacing: 0.6px;
  }

  .divider {
    position: absolute;
    left: 300px;
    top: 108px;
    width: 4px;
    height: 232px;
    background: linear-gradient(to bottom, var(--divider-top), var(--divider-bottom));
  }

  .contact {
    position: absolute;
    left: 326px;
    top: 134px;
    color: var(--ink);
  }

  .contact-address {
    font-weight: 700;
    font-size: 17px;
    line-height: 1.2;
  }

  .contact-row {
    display: flex;
    align-items: center;
    gap: 8px;
    margin-top: 10px;
    font-size: 17px;
    line-height: 1.2;
    color: var(--ink-soft);
    white-space: nowrap;
  }

  .contact-icon {
    width: 20px;
    height: 16px;
    flex: none;
  }

  .contact-web {
    margin-top: 14px;
    font-weight: 900;
    font-size: 20px;
    color: var(--ink);
  }
</style>
</head>
<body>
<main class="sheet">

  <section class="card card--back">
    <div class="services-photos">
      <div class="services-photo services-photo--table" role="img" aria-label="Photo of a blue floral table arrangement"></div>
      <div class="services-photo services-photo--posy" role="img" aria-label="Photo of a lilac and white wedding posy on a timber floor"></div>
      <div class="services-photo services-photo--roses" role="img" aria-label="Photo of peach and white roses on greenery"></div>
    </div>
    <p class="services-list">
      Bridal Bouquet, Bridesmaid Bouquets,<br>
      Flower Girl Bouquets, Ceremony Flowers<br>
      &amp; Wedding Reception Flowers
    </p>
  </section>

  <section class="card card--front">
    <div class="brand">
      <div class="brand-name"><span class="brand-dot"></span><span>Petal &amp; Thread</span></div>
      <div class="brand-tagline">Floral Designer</div>
    </div>

    <div class="holder">
      <div class="holder-name">YOUR NAME</div>
      <div class="holder-role">DESIGNATION</div>
    </div>

    <div class="divider"></div>

    <div class="contact">
      <div class="contact-address">Your Complete<br>Address Details Here</div>
      <div class="contact-row">
        <svg class="contact-icon" viewBox="0 0 20 16" aria-hidden="true">
          <path d="M3 4 C3 2 5 1 7 1 H13 C15 1 17 2 17 4 V5 H13 V3.5 H7 V5 H3 Z" fill="#6e6e6e"/>
          <rect x="4" y="7" width="12" height="8" rx="1.5" fill="#6e6e6e"/>
        </svg>
        <span>+61 417 635 208</span>
      </div>
      <div class="contact-row">
        <svg class="contact-icon" viewBox="0 0 20 16" aria-hidden="true">
          <rect x="1" y="2" width="18" height="12" fill="#6e6e6e"/>
          <path d="M1 2 L10 9 L19 2" fill="none" stroke="#f7f7f7" stroke-width="1.5"/>
        </svg>
        <span>lornajayne@petalandthread.com.au</span>
      </div>
      <div class="contact-web">www.petalandthread.com.au</div>
    </div>
  </section>

</main>
</body>
</html>
```